Comprehensive Wealth Management

We provide the following services:
Asset Protection
Trust Administration
Estate Planning - Wills & Trusts
Management of Assets, Stocks, Bonds, ETF's, and Mutual Funds
Tax Planning
Financial Planning
Multi-Generational Planning
Business Planning
Retirement Planning
Risk Management
Hi Designers, please see the attached link for a sample of our website that you can see what we do and you may or may not use the same colors and style. Be creative please.
http://peterholloway.sitevale-example.com/

Target Market(s)

Widows, Trust beneficiaries, Trustees, retirees and those getting ready for retirement

Contact Information for Business Card

Law Offices of Peter M. Holloway
48217 Corliss Avenue, Suite 206
Woodland Hills, California 91379
p: 818.555.4216
f: 818.555.4290
e: pholloway@fernwickadv.com

Peter M. Holloway, Esq., CPA, CFP

Colors
0293ce
33a6d7
86cae7
0555a3
3377b5
85acd3
00a990
34b8a4
87d0c7

Requirements
Must have
• I would like a design that really pops. I have a sample brochure that has a molecular structure with the various topics on each molecule. I like the various shades of blue. I can send you the brochure sample if you like.
Nice to have
• Very high end design/logo of some kind that has a modern art look. We primarily work with high net worth and ultra high net worth clients. It should be unique looking. Maybe with pretty greens and blues.

```html
<!DOCTYPE html>
<html lang="en">
<head>
<meta charset="utf-8">
<title>Peter M. Holloway – Business Card</title>
<link rel="stylesheet" href="https://fonts.googleapis.com/css2?family=Oswald:wght@300;400;700&family=Asap:wght@400&display=swap">
<style>
  :root {
    --canvas: #ffffff;
    --panel-light: #e6e6e8;
    --panel-dark: #333133;
    --card-white: #ffffff;
    --ink-dark: #333133;
    --brand-blue: #3d5a8a;
    --line-white: #ffffff;
  }
  html, body {
    margin: 0;
    padding: 0;
    width: 1200px;
    height: 1125px;
    overflow: hidden;
    background: var(--canvas);
  }
  .stage { position: relative; width: 1200px; height: 1125px; }
  .panel { position: absolute; }
  .panel--front { left: 20px; top: 72px; width: 573px; height: 980px; background: var(--panel-light); }
  .panel--back { left: 609px; top: 72px; width: 575px; height: 985px; background: var(--panel-dark); }

  .card { position: absolute; background: var(--card-white); }
  .card--front { left: 67px; top: 121px; width: 477px; height: 882px; }
  .card--back { left: 660px; top: 123px; width: 470px; height: 888px; }

  .hero { position: absolute; left: 85px; top: 139px; width: 441px; height: 525px; background: var(--ink-dark); overflow: hidden; }
  .hero-divider { position: absolute; left: 0; top: 0; width: 441px; height: 525px; }

  .brand-name {
    position: absolute;
    font-family: "Oswald", sans-serif;
    font-weight: 400;
    white-space: nowrap;
    text-align: center;
    line-height: 1;
  }
  .brand-name--front { left: 85px; width: 441px; top: 255px; font-size: 48px; color: var(--brand-blue); }
  .brand-name--back { left: 677px; width: 436px; top: 910px; font-size: 48px; color: var(--line-white); }

  .person { position: absolute; left: 108px; top: 562px; color: var(--line-white); }
  .person-name {
    font-family: "Oswald", sans-serif;
    font-size: 40px;
    line-height: 1;
    margin: 0;
    white-space: nowrap;
  }
  .person-name .given { font-weight: 300; }
  .person-name .family { font-weight: 700; }
  .person-credentials {
    font-family: "Asap", sans-serif;
    font-size: 20px;
    margin: 8px 0 0 3px;
  }

  .office-title {
    position: absolute; left: 85px; width: 441px; top: 672px;
    font-family: "Oswald", sans-serif; font-weight: 400;
    font-size: 46px; line-height: 1; text-align: center;
    color: var(--ink-dark); margin: 0;
  }

  .contact { position: absolute; left: 85px; top: 742px; width: 441px; height: 244px; background: var(--brand-blue); }
  .contact-item {
    position: absolute; left: 70px;
    font-family: "Asap", sans-serif; font-size: 18px; line-height: 20.5px;
    color: var(--line-white); white-space: nowrap;
  }
  .contact-icon { position: absolute; left: 24px; width: 28px; height: 28px; }

  .back-field { position: absolute; left: 677px; top: 140px; width: 436px; height: 854px; background: var(--brand-blue); }
</style>
</head>
<body>
<div class="stage">
  <div class="panel panel--front"></div>
  <div class="panel panel--back"></div>

  <!-- Front of card -->
  <div class="card card--front"></div>
  <div class="hero">
    <svg class="hero-divider" viewBox="0 0 441 525" aria-hidden="true">
      <polygon points="0,420 441,250 441,525 0,525" fill="var(--brand-blue)"/>
      <line x1="0" y1="420" x2="441" y2="250" stroke="var(--line-white)" stroke-width="8"/>
    </svg>
  </div>
  <div class="brand-name brand-name--front">HOLLOWAY LAW</div>

  <div class="person">
    <h1 class="person-name"><span class="given">PETER M.</span> <span class="family">HOLLOWAY</span></h1>
    <p class="person-credentials">Esq., CPA, CFP</p>
  </div>

  <h2 class="office-title">THE LAW OFFICES</h2>

  <div class="contact">
    <svg class="contact-icon" style="top:10px" viewBox="0 0 28 28" aria-label="Phone">
      <path d="M2 9 Q14 1 26 9 L23 13 L19 11 L19 9 Q14 7 9 9 L9 11 L5 13 Z" fill="var(--line-white)"/>
      <path d="M7 14 L10 11 L18 11 L21 14 L22 23 L6 23 Z" fill="var(--line-white)"/>
      <g fill="var(--brand-blue)"><rect x="11" y="15" width="2" height="2"/><rect x="15" y="15" width="2" height="2"/><rect x="11" y="19" width="2" height="2"/><rect x="15" y="19" width="2" height="2"/></g>
    </svg>
    <div class="contact-item" style="top:2px">541.555.4216<br>541.555.4290</div>

    <svg class="contact-icon" style="top:61px" viewBox="0 0 28 28" aria-label="Email">
      <rect x="3" y="6" width="22" height="16" fill="none" stroke="var(--line-white)" stroke-width="2"/>
      <path d="M3 6 L14 16 L25 6 M3 22 L11 13 M25 22 L17 13" fill="none" stroke="var(--line-white)" stroke-width="1.6"/>
    </svg>
    <div class="contact-item" style="top:63px">pholloway@fernwickadv.com</div>

    <svg class="contact-icon" style="top:103px" viewBox="0 0 28 28" aria-label="Website">
      <rect x="3" y="5" width="22" height="15" fill="none" stroke="var(--line-white)" stroke-width="2.4"/>
      <rect x="12" y="20" width="4" height="3" fill="var(--line-white)"/>
      <rect x="8" y="23" width="12" height="2" fill="var(--line-white)"/>
    </svg>
    <div class="contact-item" style="top:105px">www.peterholloway.sitevale-example.com</div>

    <svg class="contact-icon" style="top:163px" viewBox="0 0 28 28" aria-label="Address">
      <path d="M14 2 C8.5 2 5 6 5 10.5 C5 16 14 26 14 26 C14 26 23 16 23 10.5 C23 6 19.5 2 14 2 Z" fill="var(--line-white)"/>
      <circle cx="14" cy="10.5" r="3.4" fill="var(--brand-blue)"/>
    </svg>
    <div class="contact-item" style="top:146px">Law Offices of Peter M. Holloway<br>48217 Corliss Avenue, Suite 206<br>Harlow Springs, Oregon 97410</div>
  </div>

  <!-- Back of card -->
  <div class="card card--back"></div>
  <div class="back-field"></div>
  <div class="brand-name brand-name--back">HOLLOWAY LAW</div>
</div>
</body>
</html>
```